Looking for highly visual rework of current Maple Hollow Lodges Wordpress site

Visually Appealing, high tech rework of an existing wordpress site - I want an exquisite sales tool for these gorgeous tiny houses.

Must have the ability to apply various colors and styles to model homes during the sales process. We need to easily create, view, change and save home and color configurations for customers. [Roof Color, Siding, Trim, etc]

Target Market(s)

women, 50 and up

Coding

Coded - Design and coding required

Number of Pages Required

1 page

Font styles to use
Serif

Requirements
Must have
• wordpress compatability
• video of Maple Hollow intro

```html
<!DOCTYPE html>
<html lang="en">
<head>
<meta charset="utf-8">
<title>Maple Hollow Lodges</title>
<link href="https://fonts.googleapis.com/css2?family=Old+Standard+TT:wght@400;700&family=Libre+Baskerville:wght@400;700&display=swap" rel="stylesheet">
<style>
:root{
  --orange:#c2552a;
  --orange-dark:#9e3f1b;
  --brown:#5b3420;
  --ink:#2f241d;
  --body:#4a3d33;
  --cream:#f3ebe2;
  --sky-light:#f1e8df;
  --sky-mid:#ddd0c3;
  --white:#ffffff;
  --gold:#d9b98a;
}
*{margin:0;padding:0;box-sizing:border-box}
html,body{width:1200px;height:4876px;overflow:hidden}
body{
  position:relative;
  font-family:"Libre Baskerville",Georgia,serif;
  color:var(--body);
  background:
    radial-gradient(ellipse at 20% 25%,#f8f2ec 0,transparent 40%),
    radial-gradient(ellipse at 80% 55%,#f6efe7 0,transparent 40%),
    linear-gradient(180deg,var(--sky-light) 0%,var(--sky-mid) 30%,var(--sky-light) 50%,var(--sky-mid) 75%,var(--sky-light) 100%);
}
.abs{position:absolute}
.photo{position:absolute;display:block}
.serif-head{font-family:"Old Standard TT",Georgia,serif;color:var(--ink);text-align:center;position:absolute;left:0;width:1200px}

/* hero */
.hero{left:0;top:0;width:1200px;height:760px;
  background:linear-gradient(180deg,#7c8fa6 0%,#b2a197 28%,#b8693c 55%,#8a3e1f 80%,#5a2a17 100%)}
.topbar{left:180px;top:14px;width:840px;height:40px;display:flex;align-items:center;justify-content:space-between;color:var(--white);font-size:17px}
.topbar .contact{display:flex;gap:26px;align-items:center}
.topbar .item{display:flex;gap:8px;align-items:center}
.socials{display:flex;gap:8px}
.socials span{width:22px;height:22px;border-radius:50%;background:var(--white);opacity:.9;display:block}
.nav{position:absolute;left:260px;top:88px;width:680px;height:40px;background:var(--orange);display:flex;justify-content:center;align-items:center;gap:30px;font-size:11px;letter-spacing:1px;color:var(--white);text-transform:uppercase}
.nav.footer-nav{left:0;top:4512px;width:1200px;height:48px}
.hero-title{position:absolute;left:150px;top:160px;width:900px;text-align:center;font-family:"Old Standard TT",Georgia,serif;font-weight:700;font-size:58px;line-height:64px;color:var(--white);text-shadow:0 3px 8px rgba(0,0,0,.45)}
.btn{position:absolute;display:flex;align-items:center;justify-content:center;background:var(--white);color:var(--ink);font-family:"Old Standard TT",Georgia,serif;font-weight:700;border-radius:32px;border:3px solid var(--orange);box-shadow:0 4px 10px rgba(0,0,0,.3)}
.hero-btn{left:460px;top:504px;width:280px;height:68px;font-size:28px}
.brand{position:absolute;display:flex;align-items:center;justify-content:center;gap:14px;font-family:"Old Standard TT",Georgia,serif;font-weight:700;color:var(--brown)}
.brand i{display:block;width:26px;height:26px;border-radius:50%;background:var(--orange);flex:none}
.hero-brand{left:400px;top:650px;width:400px;height:80px;font-size:40px;color:var(--white)}

/* about */
.about-photo{left:220px;top:1048px;width:332px;height:264px;border:6px solid var(--white);box-shadow:0 2px 8px rgba(0,0,0,.25);background:linear-gradient(180deg,#8fa6b8,#7d6d5e 60%,#5d5148)}
.para{position:absolute;font-size:14px;line-height:22px;color:var(--body)}
.small-btn{position:absolute;display:flex;align-items:center;justify-content:center;border:2px solid var(--gold);background:var(--white);font-size:13px;color:var(--ink)}

/* cabins */
.cabins-panel{left:100px;top:1572px;width:1008px;height:588px;background:var(--white);box-shadow:0 2px 10px rgba(0,0,0,.12)}
.cabin{position:absolute;top:1608px;width:232px;height:392px}
.cabin-text{position:absolute;top:2032px;width:232px;font-size:13px;line-height:20px;color:var(--body)}

/* kitchen */
.kitchen{left:0;top:2352px;width:1200px;height:608px;background:linear-gradient(135deg,#c99867 0%,#b07a4a 40%,#8a5a34 70%,#2c2622 100%)}
.kitchen-btn{left:460px;top:2820px;width:280px;height:68px;font-size:28px}

/* gallery */
.g-item{position:absolute;width:352px;border-radius:22px;border:4px solid var(--gold);overflow:hidden}

/* newsletter */
.news-band{left:0;top:3840px;width:1200px;height:672px;background:linear-gradient(180deg,#c9c1b8 0%,#a5653a 30%,#b0703f 60%,#8a4f2a 85%,#d8cfc6 100%)}
.news-box{position:absolute;left:128px;top:3880px;width:384px;height:420px;background:rgba(40,28,22,.72);border-radius:16px;padding:28px 32px}
.news-box h3{font-family:"Old Standard TT",Georgia,serif;font-weight:400;color:var(--white);font-size:32px;margin-bottom:22px}
.field{height:56px;background:var(--white);margin-bottom:16px;display:flex;align-items:center;padding-left:18px;font-size:16px;color:var(--ink)}
.send{width:190px;height:56px;margin:8px auto 0;background:var(--orange);color:var(--white);font-family:"Old Standard TT",Georgia,serif;font-weight:700;font-size:26px;display:flex;align-items:center;justify-content:center;letter-spacing:1px}

/* footer */
.footer{left:0;top:4560px;width:1200px;height:316px;background:var(--cream)}
.footer-brand{left:100px;top:4610px;width:280px;height:180px;font-size:30px}
.footer-contact{position:absolute;left:840px;font-size:20px;color:var(--ink);display:flex;align-items:center;gap:14px}
.icon-dot{width:34px;height:34px;border-radius:50%;background:var(--ink);display:flex;align-items:center;justify-content:center}
.footer-socials{position:absolute;left:856px;top:4752px;display:flex;gap:10px}
.footer-socials span{width:28px;height:28px;border-radius:50%;background:var(--brown);display:block}
</style>
</head>
<body>

<!-- Hero -->
<div class="photo hero" role="img" aria-label="Red rock canyon landscape under a cloudy blue sky"></div>
<div class="abs topbar">
  <div class="contact">
    <div class="item">
      <svg width="20" height="20" viewBox="0 0 24 24" fill="#fff"><path d="M6.6 10.8a15.1 15.1 0 0 0 6.6 6.6l2.2-2.2c.3-.3.7-.4 1-.2 1.1.4 2.3.6 3.6.6.6 0 1 .4 1 1V20c0 .6-.4 1-1 1C10.6 21 3 13.4 3 4c0-.6.4-1 1-1h3.5c.6 0 1 .4 1 1 0 1.3.2 2.5.6 3.6.1.3 0 .7-.2 1z"/></svg>
      <span>123 456 789</span>
    </div>
    <div class="item">
      <svg width="20" height="16" viewBox="0 0 24 18" fill="none" stroke="#fff" stroke-width="2"><rect x="1" y="1" width="22" height="16"/><path d="M1 1l11 9 11-9"/></svg>
      <span>info@maplehollow.com</span>
    </div>
  </div>
  <div class="socials"><span></span><span></span><span></span><span></span><span></span></div>
</div>
<nav class="nav"><span>Home</span><span>About Us</span><span>Cabins</span><span>Activations</span><span>Gallery</span><span>Contact Us</span></nav>
<h1 class="hero-title">Lorem ipsum dolor sit amet, consectetur adipiscing elit.</h1>
<div class="btn hero-btn">Contact Us</div>
<div class="brand hero-brand"><i></i>Maple Hollow</div>

<!-- About -->
<h2 class="serif-head" style="top:928px;font-size:32px;font-weight:400">ABOUT US</h2>
<div class="photo about-photo" role="img" aria-label="Portrait of the company owner outdoors"></div>
<p class="para" style="left:600px;top:1052px;width:400px">Lorem ipsum dolor sit amet, consectetur adipiscing elit. Sed egestas tristique mauris, sed vehicula ex fermentum dictum. Curabitur in tincidunt ligula. Morbi venenatis vel est eu ultrices. Suspendisse ornare mauris et justo rutrum blandit. Donec facilisis libero venenatis, ornare magna in, pharetra eros. Suspendisse ac magna neque.</p>
<div class="small-btn" style="left:600px;top:1296px;width:180px;height:40px">More About Us</div>

<!-- Cabins -->
<h2 class="serif-head" style="top:1420px;font-size:34px;font-weight:400">OUR</h2>
<h2 class="serif-head" style="top:1460px;font-size:64px;font-weight:400;letter-spacing:2px">CABINS</h2>
<div class="abs cabins-panel"></div>
<div class="photo cabin" style="left:124px;background:linear-gradient(180deg,#a8bfd4 0%,#a8bfd4 30%,#a4512c 45%,#7e3b22 80%,#777 100%)" role="img" aria-label="Red-sided tiny house exterior"></div>
<div class="photo cabin" style="left:372px;background:linear-gradient(180deg,#b8c6d0 0%,#c06a3e 30%,#8c6a4e 60%,#6e5f52 100%)" role="img" aria-label="Tiny house with screened porch"></div>
<div class="photo cabin" style="left:620px;background:linear-gradient(180deg,#c9b9a8 0%,#6b4a36 35%,#8a7260 70%,#5c4e44 100%)" role="img" aria-label="Cabin porch with wooden door"></div>
<div class="photo cabin" style="left:868px;background:linear-gradient(180deg,#7a6a5d 0%,#a7623a 30%,#c07a47 65%,#d9d0c4 100%)" role="img" aria-label="Wood cabin front with entry steps"></div>
<p class="cabin-text" style="left:124px">Lorem ipsum dolor sit amet, consectetur adipiscing elit. Sed egestas tristique mauris.</p>
<p class="cabin-text" style="left:372px">Lorem ipsum dolor sit amet, consectetur adipiscing elit. Sed egestas tristique mauris.</p>
<p class="cabin-text" style="left:620px">Lorem ipsum dolor sit amet, consectetur adipiscing elit. Sed egestas tristique mauris.</p>
<p class="cabin-text" style="left:868px">Lorem ipsum dolor sit amet, consectetur adipiscing elit. Sed egestas tristique mauris.</p>

<!-- Luxury -->
<h2 class="serif-head" style="top:2214px;font-size:32px;font-weight:400">LUXURY &amp;</h2>
<h2 class="serif-head" style="top:2256px;font-size:58px;font-weight:400;letter-spacing:2px">COMFORT</h2>
<div class="photo kitchen" role="img" aria-label="Knotty pine cabin kitchen with dark appliances"></div>
<div class="btn kitchen-btn">Contact Us</div>

<!-- Gallery -->
<h2 class="serif-head" style="top:3034px;font-size:34px;font-weight:400">OUR</h2>
<h2 class="serif-head" style="top:3072px;font-size:62px;font-weight:400;letter-spacing:2px">GALLERY</h2>
<div class="photo g-item" style="left:48px;top:3188px;height:264px;background:linear-gradient(180deg,#3c3836,#9c5634 45%,#7a4a30 80%,#b5aca2)" role="img" aria-label="Cabin displayed in showroom"></div>
<div class="photo g-item" style="left:424px;top:3188px;height:264px;background:linear-gradient(180deg,#8fa1b0,#a05a36 40%,#6e6a60 75%,#b7ad9f)" role="img" aria-label="Cabin with gray porch outdoors"></div>
<div class="photo g-item" style="left:796px;top:3188px;height:264px;background:linear-gradient(180deg,#b5c6d3,#8f3525 40%,#a3502f 75%,#9a9286)" role="img" aria-label="Red-roofed cabin on a lot"></div>
<div class="photo g-item" style="left:48px;top:3468px;height:272px;background:linear-gradient(180deg,#2e2c2a,#4f5a52 40%,#8c7a66 75%,#a59a8c)" role="img" aria-label="Green-trimmed cabin indoors"></div>
<div class="photo g-item" style="left:424px;top:3468px;height:272px;background:linear-gradient(180deg,#b8c8d2,#d6d8d6 40%,#8a7564 80%,#6e5a4a)" role="img" aria-label="Cabin interior with large windows"></div>
<div class="photo g-item" style="left:796px;top:3468px;height:272px;background:linear-gradient(180deg,#b8cbd8,#8c3a28 35%,#c9b7a0 70%,#7d8a5a)" role="img" aria-label="Gazebo cabin with white railing"></div>
<div class="small-btn" style="left:520px;top:3774px;width:160px;height:36px;font-size:12px;letter-spacing:1px">VIEW MORE</div>

<!-- Newsletter -->
<div class="photo news-band" role="img" aria-label="Wooden tiny house with screened porch and white steps"></div>
<form class="news-box">
  <h3>Subscribe Newsletter</h3>
  <div class="field">Name</div>
  <div class="field">Phone</div>
  <div class="field">Email</div>
  <div class="send">SEND</div>
</form>

<!-- Footer -->
<nav class="nav footer-nav"><span>Home</span><span>About Us</span><span>Cabins</span><span>Activations</span><span>Gallery</span><span>Contact Us</span></nav>
<div class="abs footer"></div>
<div class="brand footer-brand"><i></i>Maple Hollow</div>
<p class="para" style="left:388px;top:4612px;width:420px;font-size:13px;line-height:20px">Lorem ipsum dolor sit amet, consectetur adipiscing elit. Sed egestas tristique mauris, sed vehicula ex fermentum dictum. Curabitur in tincidunt ligula. Morbi venenatis vel est eu ultrices. Suspendisse ornare mauris et justo rutrum blandit. Donec facilisis libero venenatis, ornare magna in, pharetra eros. Suspendisse ac magna neque.</p>
<div class="footer-contact" style="top:4620px">
  <span class="icon-dot"><svg width="18" height="18" viewBox="0 0 24 24" fill="#fff"><path d="M6.6 10.8a15.1 15.1 0 0 0 6.6 6.6l2.2-2.2c.3-.3.7-.4 1-.2 1.1.4 2.3.6 3.6.6.6 0 1 .4 1 1V20c0 .6-.4 1-1 1C10.6 21 3 13.4 3 4c0-.6.4-1 1-1h3.5c.6 0 1 .4 1 1 0 1.3.2 2.5.6 3.6.1.3 0 .7-.2 1z"/></svg></span>
  <span>123 456 789</span>
</div>
<div class="footer-contact" style="top:4680px">
  <span class="icon-dot"><svg width="18" height="14" viewBox="0 0 24 18" fill="none" stroke="#fff" stroke-width="2"><rect x="1" y="1" width="22" height="16"/><path d="M1 1l11 9 11-9"/></svg></span>
  <span>info@maplehollow.com</span>
</div>
<div class="footer-socials"><span></span><span></span><span></span><span></span><span></span></div>

</body>
</html>
```